The Mossy Lantern Website Redesign

I want a new design and website for www.themossylanternvelbrook.com where part of the home page includes our daily specials from our POS Tally to be pulled from API. I have included photos and links to give you a better feel for the style of our restaurant.

```html
<!DOCTYPE html>
<html lang="en">
<head>
<meta charset="utf-8">
<title>The Mossy Lantern – A Finer Diner</title>
<link href="https://fonts.googleapis.com/css2?family=Amatic+SC:wght@700&family=Caveat:wght@600&family=Poppins:wght@400;500;600;700&display=swap" rel="stylesheet">
<style>
:root{
  --red:#e10a0a;
  --black:#0a0a0a;
  --ink:#1c1c1c;
  --grey:#f4f4f4;
  --white:#ffffff;
}
*{box-sizing:border-box;margin:0;padding:0}
html,body{width:1200px;height:4850px;overflow:hidden}
body{font-family:"Poppins",sans-serif;color:var(--ink);background:var(--white);position:relative}
.abs{position:absolute}
.ph{position:absolute}
.btn{position:absolute;background:var(--red);color:var(--white);font-weight:700;font-size:14px;text-transform:uppercase;display:flex;align-items:center;justify-content:center;letter-spacing:.3px}
.btn-outline{position:absolute;border:2px solid var(--red);color:var(--red);font-weight:700;font-size:12px;text-transform:uppercase;display:flex;align-items:center;justify-content:center;background:var(--white)}
.arrow{position:absolute;width:42px;height:42px;border:2px solid var(--ink);border-radius:50%;display:flex;align-items:center;justify-content:center}

.section-title{position:absolute;left:0;width:1200px;text-align:center}
.section-title h2{font-family:"Amatic SC",cursive;font-size:66px;line-height:1;color:var(--ink)}
.section-title p{font-family:"Caveat",cursive;font-size:22px;line-height:1.2;margin-top:6px}

/* header */
.brand{left:90px;top:36px;font-size:32px;font-weight:700;color:var(--ink);line-height:1}
.brand small{display:block;font-size:15px;font-weight:700;margin-top:6px}
.call{left:755px;top:30px;display:flex;align-items:center;gap:10px;font-size:14px;font-weight:600;line-height:1.2}
.call b{display:block;font-size:12px}
.nav a{position:absolute;top:98px;color:var(--ink);text-decoration:none;font-size:17px;font-weight:500;white-space:nowrap}

/* hero */
.hero{left:0;top:151px;width:1200px;height:605px;background:linear-gradient(90deg,#050505 0%,#111 40%,#3a2a1c 70%,#1a120c 100%)}
.hero-photo{left:480px;top:151px;width:720px;height:605px;background:radial-gradient(ellipse at 55% 50%,#b07a3a 0%,#6b4322 35%,#2a1a10 70%,rgba(10,10,10,0) 100%)}
.hero-title{left:125px;top:330px;color:var(--white)}
.hero-title h1{font-family:"Amatic SC",cursive;font-size:96px;line-height:.9}
.hero-title p{font-family:"Caveat",cursive;font-size:44px;margin-top:4px}

/* specials */
.card{position:absolute;top:995px;width:296px;height:442px;background:var(--grey)}
.card .ph{left:0;top:0;width:296px;height:190px}
.card h3{position:absolute;left:25px;top:220px;font-family:"Amatic SC",cursive;font-size:32px;color:var(--ink)}
.card .price{position:absolute;right:25px;top:220px;font-family:"Amatic SC",cursive;font-size:32px;color:var(--red)}
.card p{position:absolute;left:25px;top:274px;width:250px;font-size:13px;line-height:1.45;color:#333}
.card .btn-outline{left:25px;top:365px;width:126px;height:42px}

/* about */
.about{left:0;top:1564px;width:1200px;height:668px;background:var(--black)}
.about-text{left:573px;top:1685px;width:495px;color:var(--white)}
.about-text h2{font-family:"Amatic SC",cursive;font-size:62px;line-height:1}
.about-text .tag{font-family:"Caveat",cursive;font-size:20px;margin-top:4px}
.about-text p{font-size:14px;line-height:1.68;margin-top:22px}

/* latest */
.dish{position:absolute;top:2500px;width:216px;text-align:center}
.dish .circle{width:216px;height:216px;border-radius:50%}
.dish h4{font-size:18px;font-weight:600;margin-top:28px}
.dish a{font-size:13px;color:var(--red);font-weight:600;text-decoration:none;display:inline-block;margin-top:4px}

/* features */
.features{left:0;top:3088px;width:1200px;height:436px;background:var(--red)}
.feature{position:absolute;top:3190px;width:300px;height:250px;background:var(--white)}
.feature .inner{position:absolute;left:20px;top:42px;width:260px;height:188px;border:2px dotted var(--red);text-align:center;padding-top:50px}
.feature h3{font-family:"Amatic SC",cursive;font-size:40px;color:var(--ink);line-height:1}
.feature p{font-size:14px;line-height:1.3;color:#333;margin:12px auto 0;width:210px}

/* booking */
.book-title{left:627px;top:3670px}
.book-title h2{font-family:"Amatic SC",cursive;font-size:62px;line-height:1}
.book-title p{font-family:"Caveat",cursive;font-size:20px;margin-top:4px}
.field{position:absolute;background:var(--grey);font-size:12px;color:#333;padding:14px 16px;display:flex;justify-content:space-between}

/* footer */
.footer-bg{left:0;top:4296px;width:1200px;height:554px;background:linear-gradient(180deg,#050505 0%,#1a1a1a 60%,#2b2b2b 100%)}
.footer-col{position:absolute;color:var(--white)}
.footer-col h4{font-family:"Amatic SC",cursive;font-size:44px;line-height:1;margin-bottom:22px}
.footer-links{list-style:none;font-size:14px;line-height:1.78}
.contact-row{display:flex;gap:14px;font-size:14px;line-height:1.6;margin-bottom:12px;align-items:flex-start}
</style>
</head>
<body>

<header>
  <div class="abs brand">The Mossy Lantern<small>a finer diner</small></div>
  <div class="abs call">
    <svg width="30" height="26" viewBox="0 0 30 26"><path d="M2 9c4-6 22-6 26 0l-4 4-5-3V7H11v3l-5 3z" fill="#e10a0a"/><rect x="7" y="13" width="16" height="11" rx="2" fill="#e10a0a"/><circle cx="15" cy="18.5" r="3" fill="#fff"/></svg>
    <div><b>CALL US:</b>(555) 014-2280</div>
  </div>
  <div class="btn" style="left:955px;top:26px;width:153px;height:46px">Order Online</div>
  <nav class="nav">
    <a style="left:485px">Home</a>
    <a style="left:585px">About Us</a>
    <a style="left:710px">Menu</a>
    <a style="left:810px">Retail</a>
    <a style="left:912px">Press</a>
    <a style="left:1010px">Contact Us</a>
  </nav>
</header>

<section>
  <div class="abs hero"></div>
  <div class="ph hero-photo" role="img" aria-label="Cheeseburger with fries on a checked napkin on a wooden board"></div>
  <div class="abs hero-title">
    <h1>The Mossy Lantern</h1>
    <p>a finer diner</p>
  </div>
  <div class="btn" style="left:126px;top:525px;width:154px;height:46px">Order Online</div>
</section>

<section>
  <div class="section-title" style="top:848px">
    <h2>our daily specials</h2>
    <p>Our POS Tally</p>
  </div>
  <div class="arrow" style="left:47px;top:1069px"><svg width="12" height="14"><path d="M9 1L3 7l6 6" fill="none" stroke="#1c1c1c" stroke-width="2"/></svg></div>
  <div class="arrow" style="left:1103px;top:1069px"><svg width="12" height="14"><path d="M3 1l6 6-6 6" fill="none" stroke="#1c1c1c" stroke-width="2"/></svg></div>

  <article class="card" style="left:127px">
    <div class="ph" style="background:linear-gradient(160deg,#5a4a3a,#a66a30 55%,#3d6b2a)" role="img" aria-label="Burger with lettuce and tomato on a plate"></div>
    <h3>Burger</h3><span class="price">$29.00</span>
    <p>Lorem ipsum dolor sit ametcon sectetur adipiscing elited do eiu smod tempor incididunt.</p>
    <div class="btn-outline">Order Now</div>
  </article>
  <article class="card" style="left:452px">
    <div class="ph" style="background:linear-gradient(160deg,#5a2e18,#b4522a 50%,#d98a5c)" role="img" aria-label="Green eggs and ham with roasted potatoes"></div>
    <h3>GreenEggs&amp;Ham</h3><span class="price">$29.00</span>
    <p>Lorem ipsum dolor sit ametcon sectetur adipiscing elited do eiu smod tempor incididunt.</p>
    <div class="btn-outline">Order Now</div>
  </article>
  <article class="card" style="left:777px">
    <div class="ph" style="background:linear-gradient(160deg,#6a5a30,#c9a050 50%,#7a4a22)" role="img" aria-label="Breakfast rumble of eggs, greens and potatoes"></div>
    <h3>Rumble</h3><span class="price">$29.00</span>
    <p>Lorem ipsum dolor sit ametcon sectetur adipiscing elited do eiu smod tempor incididunt.</p>
    <div class="btn-outline">Order Now</div>
  </article>
</section>

<section>
  <div class="abs about"></div>
  <div class="ph" style="left:100px;top:1700px;width:310px;height:226px;border:4px solid #fff;background:linear-gradient(135deg,#c9b23a,#b02020 45%,#d8d4cc)" role="img" aria-label="Diner interior with red walls and counter seating"></div>
  <div class="ph" style="left:205px;top:1838px;width:322px;height:298px;border:4px solid var(--red);background:linear-gradient(160deg,#2a3a7a,#8a5a2a 50%,#c4883a)" role="img" aria-label="Waffles topped with berries and syrup"></div>
  <div class="abs about-text">
    <h2>About The Mossy Lantern</h2>
    <div class="tag">a finer dinner</div>
    <p>A finer diner were eagerly thrown open for the first time on December 28th 2004. We welcomed our first customers and started our magnificent life as a business that continues on through today. Along with our beloved and inquisitive customers came the many questions of our origin. the most important of which we will address right here and now… "Why?" they asked "Why did you name your restaurant The Mossy Lantern? We always swore we would make up some exciting folklore tale of the origin of our now venerated name, but we never quite came up with a story glorious enough to do Justice to the wonderment.</p>
  </div>
  <div class="btn" style="left:573px;top:2058px;width:154px;height:47px">Read More</div>
</section>

<section>
  <div class="section-title" style="top:2365px">
    <h2>our latest menu</h2>
    <p>the mossy lantern</p>
  </div>
  <div class="arrow" style="left:47px;top:2598px"><svg width="12" height="14"><path d="M9 1L3 7l6 6" fill="none" stroke="#1c1c1c" stroke-width="2"/></svg></div>
  <div class="arrow" style="left:1103px;top:2598px"><svg width="12" height="14"><path d="M3 1l6 6-6 6" fill="none" stroke="#1c1c1c" stroke-width="2"/></svg></div>

  <div class="dish" style="left:124px"><div class="circle" style="background:radial-gradient(circle,#f3d87a,#c9a04a 60%,#6a5a40)" role="img" aria-label="Poached eggs with herbs"></div><h4>All Things Eggs</h4><a>View All ⊕</a></div>
  <div class="dish" style="left:370px"><div class="circle" style="background:radial-gradient(circle,#e0b070,#b07a3a 60%,#6a6a6a)" role="img" aria-label="Stacked waffles with powdered sugar"></div><h4>Oh, Sugar Shack!</h4><a>View All ⊕</a></div>
  <div class="dish" style="left:615px"><div class="circle" style="background:radial-gradient(circle,#d8c080,#8a8a4a 60%,#4a5a3a)" role="img" aria-label="Stuffed mushrooms with herbs"></div><h4>Green Things</h4><a>View All ⊕</a></div>
  <div class="dish" style="left:862px"><div class="circle" style="background:radial-gradient(circle,#d49040,#a0501e 60%,#5a2a14)" role="img" aria-label="Chickpeas and roasted chicken"></div><h4>Between Bread</h4><a>View All ⊕</a></div>

  <div class="btn" style="left:507px;top:2829px;width:186px;height:47px">View All Menu</div>
  <div class="ph" style="left:0;top:2900px;width:1200px;height:190px;background:linear-gradient(180deg,rgba(255,255,255,0) 0%,#f0b48a 40%,#d2582a 70%,#5a8a3a 100%)" role="img" aria-label="Fresh ingredients: salmon, steak, eggs, tomatoes, almonds and greens"></div>
</section>

<section>
  <div class="abs features"></div>
  <div class="feature" style="left:127px"><div class="inner"><h3>Brunch</h3><p>is what we call our menu, and ALL items are available ALL hours we are open!</p></div></div>
  <div class="feature" style="left:450px"><div class="inner"><h3>Booze</h3><p>we have a Full bar! Beer, Wine and Booze_ Catch a Buzz!!!</p></div></div>
  <div class="feature" style="left:773px"><div class="inner"><h3>Plastic</h3><p>we gladly accept all major credit cards!</p></div></div>
</section>

<section>
  <div class="abs" style="left:117px;top:3830px;width:8px;height:324px;background:var(--red)"></div>
  <div class="abs" style="left:117px;top:4146px;width:270px;height:8px;background:var(--red)"></div>
  <div class="ph" style="left:133px;top:3676px;width:420px;height:463px;background:radial-gradient(ellipse at 50% 55%,#c9602a,#7a2a14 55%,#1a1a1a)" role="img" aria-label="Glazed chicken meatball skewers"></div>

  <div class="abs book-title">
    <h2>book online now</h2>
    <p>the mossy lantern</p>
  </div>
  <div class="field" style="left:627px;top:3783px;width:216px;height:48px">Name:</div>
  <div class="field" style="left:853px;top:3783px;width:216px;height:48px">Email:</div>
  <div class="field" style="left:627px;top:3847px;width:216px;height:48px">Phone:</div>
  <div class="field" style="left:853px;top:3847px;width:216px;height:48px">Menu:<span>▾</span></div>
  <div class="field" style="left:627px;top:3911px;width:216px;height:48px">Date:<span>▾</span></div>
  <div class="field" style="left:853px;top:3911px;width:216px;height:48px">Time:<span>▾</span></div>
  <div class="field" style="left:627px;top:3975px;width:442px;height:106px">Message:</div>
  <div class="btn" style="left:627px;top:4098px;width:146px;height:47px">Book Now</div>
</section>

<footer>
  <div class="abs footer-bg"></div>
  <div class="footer-col" style="left:128px;top:4420px">
    <div style="font-size:32px;font-weight:700;line-height:1">The Mossy Lantern</div>
    <div style="font-size:15px;font-weight:700;margin-top:6px">a finer diner</div>
    <p style="width:320px;font-size:14px;line-height:1.65;margin-top:26px">A finer diner were eagerly thrown open for the first time on December 28th 2004. We welcomed our first customers and started our magnificent life as a business that continues on through today.</p>
  </div>
  <div class="footer-col" style="left:580px;top:4428px">
    <h4>links</h4>
    <ul class="footer-links"><li>Home</li><li>About Us</li><li>Menu</li><li>Retail</li><li>Press</li><li>Contact Us</li></ul>
  </div>
  <div class="footer-col" style="left:825px;top:4428px;width:300px">
    <h4>contact</h4>
    <div class="contact-row"><svg width="14" height="18" viewBox="0 0 14 18"><path d="M7 0a7 7 0 0 1 7 7c0 5-7 11-7 11S0 12 0 7a7 7 0 0 1 7-7z" fill="#e10a0a"/><circle cx="7" cy="7" r="2.5" fill="#1a1a1a"/></svg><span>1840 Alder Row<br>Velbrook, Michigan 48999</span></div>
    <div class="contact-row"><svg width="16" height="16" viewBox="0 0 16 16"><path d="M3 1l3 3-2 2c1 2 3 4 5 5l2-2 3 3-2 3C7 15 1 9 1 3z" fill="#e10a0a"/></svg><span>Phone (555) 014-2280</span></div>
    <div class="contact-row"><svg width="16" height="14" viewBox="0 0 16 14"><rect x="1" y="2" width="14" height="10" fill="none" stroke="#e10a0a" stroke-width="1.6"/><path d="M1 2l7 6 7-6" fill="none" stroke="#e10a0a" stroke-width="1.6"/></svg><span>eat@themossylanternvelbrook.com</span></div>
    <div class="contact-row"><svg width="16" height="16" viewBox="0 0 16 16"><circle cx="8" cy="8" r="7" fill="none" stroke="#e10a0a" stroke-width="1.6"/><path d="M8 4v4l3 2" fill="none" stroke="#e10a0a" stroke-width="1.6"/></svg><span>Sat. - Sun. 8 a.m. - 3 p.m.</span></div>
  </div>
  <div class="abs" style="left:128px;top:4755px;width:944px;height:1px;background:#666"></div>
  <div class="abs" style="left:0;top:4792px;width:1200px;text-align:center;color:#fff;font-size:14px">© 2025 All Rights Reserved. Terms &amp; Conditions Privacy Policy</div>
</footer>

</body>
</html>
```